Brightmere email header for parts

We sell parts to the construction equipment industry. We want a header for our emails that reflect what we do. I will include what we have now but want something for parts only. Added a lot of pictures just so you can look through what we do.

```html
<!DOCTYPE html>
<html lang="en">
<head>
<meta charset="utf-8">
<title>Brightmere parts email headers</title>
<link href="https://fonts.googleapis.com/css2?family=IBM+Plex+Sans:wght@400;700&display=swap" rel="stylesheet">
<style>
:root{
  --bg:#a51e25;
  --brand-red:#bb1e2b;
  --white:#ffffff;
  --ink:#111111;
  --photo-part:linear-gradient(160deg,#8d8c87 0%,#c9a32a 45%,#7c7566 100%);
  --photo-engine:linear-gradient(160deg,#6b8a86 0%,#3f5f5c 55%,#8b8478 100%);
  --photo-bench:linear-gradient(160deg,#b8b3a6 0%,#2f58a8 50%,#6e6a62 100%);
  --photo-panel:linear-gradient(160deg,#8a8a86 0%,#e2ab1c 50%,#6f6d68 100%);
  --photo-seat:linear-gradient(160deg,#a5a39d 0%,#2a2a2a 55%,#9a9892 100%);
  --photo-shelves:linear-gradient(160deg,#d9d2c2 0%,#9a9890 40%,#cf3a30 70%,#3c5aa8 100%);
}
*{margin:0;padding:0;box-sizing:border-box}
html,body{width:1051px;height:1200px;overflow:hidden;background:var(--bg)}
body{position:relative;font-family:"IBM Plex Sans",Arial,sans-serif}
.banner{position:absolute;left:71px;width:909px;height:344px;background:var(--brand-red)}
.banner--split{top:56px}
.banner--strip{top:436px}
.banner--centered{top:815px}
.abs{position:absolute}
.white-panel{position:absolute;background:var(--white)}
.photo{position:absolute}
.photo--framed{border:3px solid var(--white)}
.brand{position:absolute;display:flex;align-items:center;gap:8px;transform:translateX(-50%);white-space:nowrap}
.brand__mark{width:14px;height:14px;background:var(--brand-red)}
.brand__text{display:flex;flex-direction:column;line-height:1}
.brand__name{font-weight:700;font-size:22px;letter-spacing:1px;color:var(--ink)}
.brand__sub{font-size:7.5px;color:var(--ink);margin-top:3px;letter-spacing:.2px}
.headline{position:absolute;transform:translateX(-50%);text-align:center;width:360px}
.headline__light{font-size:32px;font-weight:400;line-height:32px;color:var(--ink);letter-spacing:-.3px}
.headline__bold{font-size:40px;font-weight:700;line-height:38px;color:var(--brand-red);letter-spacing:-.5px}
.headline__rule{height:3px;width:274px;background:var(--ink);margin:2px auto 4px}
.phone-box{position:absolute;background:var(--brand-red);color:var(--white);font-weight:700;font-size:29px;display:flex;align-items:center;justify-content:center;transform:translateX(-50%)}
.strip-tagline{position:absolute;left:23px;top:305px;color:var(--white);font-weight:700;font-size:24px;letter-spacing:.2px;white-space:nowrap}
.strip-phone{position:absolute;left:720px;top:296px;width:166px;height:33px;background:var(--white);color:var(--brand-red);font-weight:700;font-size:21px;display:flex;align-items:center;justify-content:center}
</style>
</head>
<body>

<section class="banner banner--split">
  <div class="white-panel" style="left:0;top:0;width:415px;height:344px"></div>
  <div class="brand" style="left:208px;top:38px">
    <span class="brand__mark"></span>
    <span class="brand__text"><span class="brand__name">BRIGHTMERE</span><span class="brand__sub">CONSTRUCTION EQUIPMENT &amp; PARTS, INC.</span></span>
  </div>
  <div class="headline" style="left:194px;top:102px">
    <div class="headline__light">CUSTOM BUILT</div>
    <div class="headline__bold">WATER TANKS</div>
    <div class="headline__rule"></div>
    <div class="headline__light">REPLACEMENT</div>
    <div class="headline__bold">PARTS</div>
  </div>
  <div class="phone-box" style="left:194px;top:274px;width:234px;height:48px">555 014 2290</div>
  <div class="photo" role="img" aria-label="Yellow machined steering part on a pallet" style="left:428px;top:0;width:109px;height:108px;background:var(--photo-part)"></div>
  <div class="photo" role="img" aria-label="Yellow rebuilt transmission on a shop floor" style="left:428px;top:118px;width:109px;height:108px;background:var(--photo-panel)"></div>
  <div class="photo" role="img" aria-label="Transmission mounted on a blue test bench" style="left:428px;top:235px;width:109px;height:109px;background:var(--photo-bench)"></div>
  <div class="photo" role="img" aria-label="Warehouse shelves stocked with boxed parts and red bins" style="left:550px;top:0;width:359px;height:344px;background:var(--photo-shelves)"></div>
</section>

<section class="banner banner--strip">
  <div class="white-panel" style="left:0;top:0;width:909px;height:96px"></div>
  <div class="brand" style="left:455px;top:30px">
    <span class="brand__mark"></span>
    <span class="brand__text"><span class="brand__name">BRIGHTMERE</span><span class="brand__sub">CONSTRUCTION EQUIPMENT &amp; PARTS, INC.</span></span>
  </div>
  <div class="photo photo--framed" role="img" aria-label="Used diesel engine" style="left:15px;top:124px;width:212px;height:150px;background:var(--photo-engine)"></div>
  <div class="photo photo--framed" role="img" aria-label="Transmission on a blue test bench" style="left:238px;top:124px;width:212px;height:150px;background:var(--photo-bench)"></div>
  <div class="photo photo--framed" role="img" aria-label="Yellow machined steering part on a pallet" style="left:460px;top:124px;width:212px;height:150px;background:var(--photo-part)"></div>
  <div class="photo photo--framed" role="img" aria-label="Yellow slotted engine side panel" style="left:683px;top:124px;width:212px;height:150px;background:var(--photo-panel)"></div>
  <div class="strip-tagline">CUSTOM BUILT WATER TANKS REPLACEMENT PARTS</div>
  <div class="strip-phone">555 014 2290</div>
</section>

<section class="banner banner--centered">
  <div class="white-panel" style="left:0;top:0;width:76px;height:345px"></div>
  <div class="photo" role="img" aria-label="Yellow machined steering part on a pallet" style="left:83px;top:0;width:153px;height:115px;background:var(--photo-part)"></div>
  <div class="photo" role="img" aria-label="Yellow slotted engine side panel" style="left:83px;top:115px;width:153px;height:114px;background:var(--photo-panel)"></div>
  <div class="photo" role="img" aria-label="Black operator seat on a pallet" style="left:83px;top:229px;width:153px;height:116px;background:var(--photo-seat)"></div>
  <div class="white-panel" style="left:243px;top:0;width:440px;height:345px"></div>
  <div class="brand" style="left:454px;top:38px">
    <span class="brand__mark"></span>
    <span class="brand__text"><span class="brand__name">BRIGHTMERE</span><span class="brand__sub">CONSTRUCTION EQUIPMENT &amp; PARTS, INC.</span></span>
  </div>
  <div class="headline" style="left:454px;top:101px">
    <div class="headline__light">CUSTOM BUILT</div>
    <div class="headline__bold">WATER TANKS</div>
    <div class="headline__rule"></div>
    <div class="headline__light">REPLACEMENT</div>
    <div class="headline__bold">PARTS</div>
  </div>
  <div class="phone-box" style="left:454px;top:275px;width:235px;height:48px">555 014 2290</div>
  <div class="photo" role="img" aria-label="Warehouse shelves stocked with boxed parts and red bins" style="left:690px;top:0;width:212px;height:345px;background:var(--photo-shelves)"></div>
</section>

</body>
</html>
```